Refreshed PPT Presentation for US based firms

There are basically 4 types of slides in this presentation:
* Roadmap (Title, Agenda, Billboards)
* Teaching (Content, Examples)
* Samples (Real life samples)
* Polls (Placeholders for interactive polls)
We want new templates for each of these types of templates with coordinated graphics, images, icons and fonts.

```html
<!DOCTYPE html>
<html lang="en">
<head>
<meta charset="utf-8">
<title>Northgate Law P.C. – Advice and Counsel through Email – Slide Templates</title>
<link href="https://fonts.googleapis.com/css2?family=Roboto:wght@300;400;500;700&display=swap" rel="stylesheet">
<style>
:root{
  --navy:#0c2152;
  --navy-2:#14306b;
  --blue:#2356b8;
  --blue-light:#8fb3e3;
  --sky:#a9c7e6;
  --ink:#1d2a44;
  --muted:#6f7f99;
  --caption:#7a8bb0;
  --paper:#ffffff;
  --bg:#ffffff;
  --accent-red:#c62828;
  --highlight:#f4ee2a;
  --tile:#dde8f6;
  --tile-dark:#4a6fb6;
}
*{box-sizing:border-box;margin:0;padding:0}
html,body{width:1200px;height:1200px;overflow:hidden;background:var(--bg);font-family:"Roboto",Arial,sans-serif;color:var(--ink)}
.deck{position:absolute;left:31px;top:92px;display:grid;grid-template-columns:repeat(4,267px);grid-template-rows:repeat(5,150px);column-gap:26px;row-gap:68.5px}
.slide{position:relative;width:267px;height:150px;background:var(--paper);overflow:hidden;box-shadow:0 4px 9px rgba(0,0,0,.28)}
.slide.dark{background:var(--navy);color:#fff}
.foot{position:absolute;left:20px;right:20px;bottom:4px;display:flex;justify-content:space-between;font-size:3.2px;color:var(--navy)}
.foot .firm{font-weight:700}
.foot .url{color:var(--muted);margin-left:14px}
.foot .num{color:var(--muted)}
.dark .foot,.dark .foot .url,.dark .foot .num{color:#c9d4ea}
.dark .foot .firm{color:#fff}
.photo{position:absolute}
.wedge{position:absolute;inset:0;width:267px;height:150px}

/* roadmap / billboard */
.billboard-title{position:absolute;left:27px;font-size:11.5px;font-weight:500;line-height:1.15;color:#fff}
.cover-firm{position:absolute;left:23px;top:43px;font-size:10px;font-weight:500;color:#fff}
.cover-title{position:absolute;left:23px;top:64px;font-size:11px;font-weight:500;line-height:1.3;color:#fff}
.cover-byline{position:absolute;left:25px;top:103px;font-size:3px;color:#dfe6f4}
.agenda-title{position:absolute;left:23px;top:17px;font-size:11px;font-weight:500}
.agenda-list{position:absolute;left:25px;top:38px;list-style:none;font-size:3.8px}
.agenda-list li{display:flex;height:15.2px;align-items:flex-start}
.agenda-list b{font-weight:400;width:17px;flex:none}
.agenda-list li.two{height:18.5px}

/* content slides */
.h2{position:absolute;font-size:9.3px;font-weight:500;color:var(--navy);line-height:1.1}
.center-h{left:0;right:0;text-align:center}
.bullets{position:absolute;list-style:none;font-size:4.4px;line-height:1.25;color:var(--blue)}
.bullets li{position:relative;padding-left:6px;margin-bottom:3.6px}
.bullets li::before{content:"";position:absolute;left:0;top:1.5px;width:1.7px;height:1.7px;border-radius:50%;background:var(--blue-light)}
.bullets.tight{font-size:3.6px}
.bullets.tight li{margin-bottom:1.6px}
.bullets .sub{list-style:none;margin-top:1.5px;font-size:3.3px}
.bullets .sub li{margin-bottom:1px}
.bullets.navy{color:var(--navy)}
.numbered{position:absolute;font-size:3.5px;line-height:1.15;color:var(--blue);padding-left:8px}
.numbered li{margin-bottom:1.8px}

/* writing steps */
.step-label{position:absolute;top:38px;width:56px;text-align:center;font-size:4.2px;font-weight:700;color:var(--navy)}
.step-img{position:absolute;top:52px;width:56px;height:45px;border:.6px solid #b9c2d4}
.step-cap{position:absolute;top:99px;width:58px;text-align:center;font-size:4.1px;line-height:1.15;color:var(--caption)}

/* email examples */
.ex-title{position:absolute;left:88px;right:0;top:10px;text-align:center;font-size:9.3px;font-weight:500;color:var(--navy)}
.meta{position:absolute;left:19px;top:28px;width:68px}
.meta-row{display:flex;font-size:3.2px;color:var(--navy);margin-bottom:4px}
.meta-row .k{width:18px;background:var(--navy);color:#fff;text-align:right;padding:1.5px 2px 0 0;flex:none}
.meta-row .v{padding:0.5px 0 0 3px;line-height:1.2}
.meta-row.r1 .k{height:11px}.meta-row.r2 .k{height:20px;padding-top:7px}.meta-row.r3 .k{height:11px;padding-top:3px}
.mailbox{position:absolute;left:88px;top:27px;width:179px;height:104px;background:var(--navy);color:#fff;padding:8px 8px 6px 8px;font-size:2.6px;line-height:1.2}
.mailbox p{margin-bottom:3px}
.mailbox mark{background:var(--highlight);color:#0c2152}
.mailbox.dense{font-size:2.5px;line-height:1.15;text-align:justify;padding:4px 5px}
.mailbox.dense p{margin-bottom:2px}
.callout{position:absolute;background:#fff;border:.6px solid var(--accent-red);color:var(--navy);font-size:3.1px;text-align:center;line-height:1.15;padding:1px 2px;box-shadow:0 0 0 .8px #fff}
.leader{position:absolute;inset:0;width:267px;height:150px}

/* nature of audience */
.node{position:absolute;width:38px;height:17px;border-radius:2px;display:flex;align-items:center;justify-content:center;font-size:4.4px;color:#fff;border:1.2px solid #e5ebf5;box-shadow:0 0 0 .5px #b8c4dd}
.node.size{background:#2f6bc4}.node.rel{background:#7fd1c4}.node.know{background:#3e4c78}.node.role{background:#4a5166}.node.con{background:#a9b5e6}

/* quick */
.quick-panel{position:absolute;left:6px;top:11px;width:122px;height:121px;background:var(--navy);color:#fff;font-size:8.5px;font-weight:500;line-height:1.15;padding:44px 0 0 12px}
.q-icon{position:absolute;left:131px;width:29px;background:var(--tile-dark);color:#fff;font-size:5.6px;text-align:center;border:1px solid #c9d6ee}
.q-icon.first{background:var(--navy)}
.q-text{position:absolute;left:160px;width:93px;background:var(--tile);font-size:4.4px;color:var(--navy);line-height:1.1;padding:10px 0 0 1px;border:1px solid #c9d6ee}

/* clear */
.clear-bar{position:absolute;left:18px;width:231px;height:15px;background:var(--navy);color:#fff;font-size:4.9px;display:flex;align-items:center;border:.7px solid #fff;box-shadow:0 1.5px 2.5px rgba(0,0,0,.35)}
.clear-bar svg{width:6px;height:6px;margin:0 11px 0 8px;flex:none}
</style>
</head>
<body>

<main class="deck">

  <!-- 1 Title -->
  <section class="slide dark" aria-label="Title slide">
    <div class="photo" style="inset:0;background:linear-gradient(100deg,#1a3266 0%,#2a4a86 45%,#5a78a8 75%,#7f95b8 100%)" role="img" aria-label="Photo of two colleagues reviewing work on a laptop in a bright office, tinted navy"></div>
    <div class="cover-firm">Northgate Law P.C.</div>
    <div class="cover-title">Advice and Counsel<br>through email</div>
    <div class="cover-byline">Dana Whitlock for Northgate Law P.C.</div>
    <div class="foot"><span></span><span class="url">Go to www.pollhub.example/danawhitlock</span><span class="num">1</span></div>
  </section>

  <!-- 2 Agenda -->
  <section class="slide dark" aria-label="Agenda">
    <svg class="wedge" viewBox="0 0 267 150">
      <defs><linearGradient id="sky" x1="0" y1="0" x2="0" y2="1"><stop offset="0" stop-color="#6f9ccb"/><stop offset="1" stop-color="#c3d8ec"/></linearGradient></defs>
      <path d="M180,0 H192 L144,60 Q134,75 146,90 L214,150 H202 L134,90 Q122,75 132,60 Z" fill="var(--blue)"/>
      <path d="M192,0 H200 L152,60 Q142,75 154,90 L222,150 H214 L146,90 Q134,75 144,60 Z" fill="#dbe6f4"/>
      <g role="img" aria-label="Photo of skydivers in formation against a blue sky"><path d="M200,0 H267 V150 H222 L154,90 Q142,75 152,60 Z" fill="url(#sky)"/></g>
    </svg>
    <div class="agenda-title">Agenda</div>
    <ol class="agenda-list">
      <li><b>01</b>Preparation and process</li>
      <li><b>02</b>Audience and purpose</li>
      <li class="two"><b>03</b>Characteristics of a quality<br>response</li>
      <li><b>03.1</b>Quick</li>
      <li><b>03.2</b>Clear</li>
      <li><b>0.3.3</b>Concise</li>
    </ol>
    <div class="foot"><span class="firm">Northgate Law P.C.</span><span class="url">Go to www.pollhub.example/danawhitlock</span><span class="num"></span></div>
  </section>

  <!-- 3 Chart -->
  <section class="slide" aria-label="Email overload chart">
    <svg class="wedge" viewBox="0 0 267 150" font-family="Roboto, sans-serif">
      <text x="80" y="21" font-size="4.4" fill="var(--blue)" text-anchor="middle">Series 1</text>
      <g font-size="2.8" fill="var(--blue)" text-anchor="end">
        <text x="26" y="31">330</text><text x="26" y="41">320</text><text x="26" y="51">310</text><text x="26" y="61">300</text><text x="26" y="71">290</text><text x="26" y="81">280</text><text x="26" y="91">270</text><text x="26" y="101">260</text><text x="26" y="111">250</text><text x="26" y="121">240</text>
      </g>
      <line x1="29" y1="120" x2="137" y2="120" stroke="#c7cfdc" stroke-width=".4"/>
      <g fill="var(--navy)">
        <rect x="32" y="90" width="16" height="30"/><rect x="54" y="78" width="16" height="42"/><rect x="76" y="66" width="16" height="54"/><rect x="98" y="53" width="16" height="67"/><rect x="120" y="38" width="16" height="82"/>
      </g>
      <g font-size="2.8" fill="var(--blue)" text-anchor="middle">
        <text x="40" y="124.5">2017</text><text x="62" y="124.5">2018</text><text x="84" y="124.5">2019</text><text x="106" y="124.5">2020</text><text x="128" y="124.5">2021</text>
      </g>
      <rect x="75" y="127.5" width="1.6" height="1.6" fill="var(--navy)"/><text x="78" y="129.1" font-size="2.5" fill="var(--blue)">Series 1</text>
    </svg>
    <div class="h2" style="left:157px;top:40px">Email overload:<br>Why!</div>
    <ul class="bullets tight" style="left:157px;top:66px;width:95px">
      <li>According to The Meridian Research Group, in 2022 333.2 billion emails were sent per day</li>
      <li>In 2018, the number of emails received per day by average worker: 121</li>
      <li>Tremendous improvement over communications in mid-1990s</li>
      <li>Easy to produce, cheap storage, efficient delivery</li>
    </ul>
    <div class="foot"><span class="firm">Northgate Law P.C.</span><span class="url">Go to www.pollhub.example/danawhitlock</span><span class="num">3</span></div>
  </section>

  <!-- 4 Example 1 -->
  <section class="slide" aria-label="Example 1">
    <div class="ex-title">Example 1</div>
    <div class="meta">
      <div class="meta-row r1"><span class="k">To</span><span class="v">Northgate on Demand</span></div>
      <div class="meta-row r2"><span class="k">From</span><span class="v">Sam Holloway<br>Associate Counsel,<br>Employment Law<br>RK Holdings</span></div>
      <div class="meta-row r3"><span class="k">Subject</span><span class="v">Medical Marijuana</span></div>
    </div>
    <div class="mailbox">
      <p>Our HR VP wants us to eliminate the company's practice of allowing employees to use marijuana at home or at work upon the employee's attestation of a medical need for medical marijuana. Some executives have complained to HR that marijuana use at work is degrading productivity and damaging our reputation with clients and potential clients.</p>
      <p>By the way, I don't allow any employees in the corporate compliance department to use marijuana under any circumstances, no matter where the employee is located. We randomly test them and fire anyone who fails the test.</p>
      <p>We want to be as restrictive as possible and make a complete 360-degree change, while complying with applicable federal and state laws. Please answer a narrow question with these facts in mind. Can we maintain a marijuana-free company? If not, what's the most we can do to duplicate my department's practice throughout the rest of the company?</p>
      <p>I have a meeting next week with the HR VP who wants to move in this direction, and I'd like to have an answer then. Can you get back to me by tomorrow?</p>
      <p>Sam</p>
    </div>
    <div class="foot"><span class="firm">Northgate Law P.C.</span><span class="url">Go to www.pollhub.example/danawhitlock</span><span class="num">4</span></div>
  </section>

  <!-- 5 Preparation billboard -->
  <section class="slide dark" aria-label="Preparation and process">
    <svg class="wedge" viewBox="0 0 267 150">
      <defs><linearGradient id="field" x1="0" y1="0" x2="0" y2="1"><stop offset="0" stop-color="#7fa049"/><stop offset=".35" stop-color="#8a7a5e"/><stop offset="1" stop-color="#6e5f4d"/></linearGradient></defs>
      <path d="M180,0 H192 L144,60 Q134,75 146,90 L214,150 H202 L134,90 Q122,75 132,60 Z" fill="var(--blue)"/>
      <path d="M192,0 H200 L152,60 Q142,75 154,90 L222,150 H214 L146,90 Q134,75 144,60 Z" fill="#dbe6f4"/>
      <g role="img" aria-label="Photo of a tractor ploughing a field"><path d="M200,0 H267 V150 H222 L154,90 Q142,75 152,60 Z" fill="url(#field)"/></g>
    </svg>
    <div class="billboard-title" style="top:75px">Preparation<br>and process</div>
    <div class="foot"><span class="firm">Northgate Law P.C.</span><span class="url">Go to www.pollhub.example/danawhitlock</span><span class="num"></span></div>
  </section>

  <!-- 6 Four stages -->
  <section class="slide" aria-label="Four stages of the writing process">
    <div class="h2 center-h" style="top:11px">Four stages of the writing process</div>
    <div class="step-label" style="left:17px">Step 1</div>
    <div class="step-label" style="left:76px">Step 2</div>
    <div class="step-label" style="left:134px">Step 3</div>
    <div class="step-label" style="left:193px">Step 4</div>
    <div class="step-img" style="left:17px;background:linear-gradient(135deg,#f4f4f4,#d8d8d8)" role="img" aria-label="Illustration of a head silhouette surrounded by thought bubbles"></div>
    <div class="step-img" style="left:76px;background:linear-gradient(135deg,#e9dfc9,#b08a5a)" role="img" aria-label="Photo of a drafting board with rulers"></div>
    <div class="step-img" style="left:134px;background:linear-gradient(135deg,#f6f3ee,#c7895a)" role="img" aria-label="Photo of a claw hammer"></div>
    <div class="step-img" style="left:193px;background:linear-gradient(135deg,#3a4f8c,#9a6a3c)" role="img" aria-label="Photo of a judge's gavel"></div>
    <div class="step-cap" style="left:16px">Madman, the creative force who generates the ideas</div>
    <div class="step-cap" style="left:75px">Architect, the planner who builds the structure for the document</div>
    <div class="step-cap" style="left:133px">Carpenter, the craftsman who writes a draft</div>
    <div class="step-cap" style="left:192px">Judge, the reviewer who edits the draft</div>
    <div class="foot"><span class="firm">Northgate Law P.C.</span><span class="url">Go to www.pollhub.example/danawhitlock</span><span class="num">6</span></div>
  </section>

  <!-- 7 Clarify -->
  <section class="slide" aria-label="Clarify the question and the timing">
    <div class="h2" style="left:25px;top:26px">Clarify the question<br>and the timing</div>
    <ul class="bullets tight navy" style="left:25px;top:50px;width:82px;color:var(--blue)">
      <li>Sometimes a little clarity is required</li>
      <li>Seek clarity in, egads, a phone call or a short email</li>
      <li>Then confirm the scope of the inquiry in an email
        <ul class="sub">
          <li>In scope: Address ability to restrict marijuana use in six states</li>
          <li>Out of scope: consequences of past practices in compliance department</li>
          <li>Timing</li>
        </ul>
      </li>
    </ul>
    <div class="photo" style="left:120px;top:34px;width:120px;height:80px;background:radial-gradient(ellipse at 55% 55%,#2a2a2a 0%,#3b3b3b 40%,#ffffff 72%)" role="img" aria-label="Photo of a black rotary telephone"></div>
    <div class="foot"><span class="firm">Northgate Law P.C.</span><span class="url">Go to www.pollhub.example/danawhitlock</span><span class="num">7</span></div>
  </section>

  <!-- 8 Example 2 highlighted -->
  <section class="slide" aria-label="Example 2 with highlights">
    <div class="ex-title">Example 2</div>
    <div class="meta">
      <div class="meta-row r1"><span class="k">To</span><span class="v">Northgate on Demand</span></div>
      <div class="meta-row r2"><span class="k">From</span><span class="v">Sam Holloway<br>Associate Counsel,<br>Employment Law<br>RK Holdings</span></div>
      <div class="meta-row r3"><span class="k">Subject</span><span class="v">Medical Marijuana</span></div>
    </div>
    <div class="mailbox">
      <p>Our HR VP wants us to eliminate the company's practice of allowing employees to use marijuana at home or at work upon the employee's attestation of a medical need for medical marijuana. Some executives have complained to HR that marijuana use at work is degrading productivity and damaging our reputation with clients and potential clients.</p>
      <p><mark>By the way, I don't allow any employees in the corporate compliance department to use marijuana under any circumstances, no matter where the employee is located. We randomly test them and fire anyone who fails the test.</mark></p>
      <p>We want to be as restrictive as possible and make a complete 360-degree change, while complying with applicable federal and state laws. Please answer a narrow question with these facts in mind. Can we maintain a marijuana-free company? If not, what's the most we can do to duplicate my department's practice throughout the rest of the company?</p>
      <p>I have a meeting next week with the HR VP who wants to move in this direction, and <mark>I'd like to have an answer then. Can you get back to me by tomorrow?</mark></p>
      <p>Sam</p>
    </div>
    <div class="foot"><span class="firm">Northgate Law P.C.</span><span class="url">Go to www.pollhub.example/danawhitlock</span><span class="num">8</span></div>
  </section>

  <!-- 9 Audience billboard -->
  <section class="slide dark" aria-label="Audience and purpose">
    <svg class="wedge" viewBox="0 0 267 150">
      <defs><linearGradient id="room" x1="0" y1="0" x2="1" y2="1"><stop offset="0" stop-color="#d9dfe8"/><stop offset=".5" stop-color="#c96a4e"/><stop offset="1" stop-color="#7c8aa8"/></linearGradient></defs>
      <path d="M180,0 H192 L144,60 Q134,75 146,90 L214,150 H202 L134,90 Q122,75 132,60 Z" fill="var(--blue)"/>
      <path d="M192,0 H200 L152,60 Q142,75 154,90 L222,150 H214 L146,90 Q134,75 144,60 Z" fill="#dbe6f4"/>
      <g role="img" aria-label="Photo of a group of people seated in a circle talking"><path d="M200,0 H267 V150 H222 L154,90 Q142,75 152,60 Z" fill="url(#room)"/></g>
    </svg>
    <div class="billboard-title" style="top:75px">Audience and<br>purpose</div>
    <div class="foot"><span class="firm">Northgate Law P.C.</span><span class="url">Go to www.pollhub.example/danawhitlock</span><span class="num"></span></div>
  </section>

  <!-- 10 Nature of audience -->
  <section class="slide" aria-label="Nature of audience">
    <div class="h2 center-h" style="top:11px">Nature of Audience</div>
    <svg class="wedge" viewBox="0 0 267 150"><circle cx="64" cy="85" r="33" fill="none" stroke="#d7e2f0" stroke-width="3.2"/></svg>
    <div class="node size" style="left:45px;top:38px">Size</div>
    <div class="node rel" style="left:12px;top:65px">Relationship</div>
    <div class="node know" style="left:81px;top:64px">Knowledge</div>
    <div class="node role" style="left:23px;top:105px">Role</div>
    <div class="node con" style="left:67px;top:105px">Concerns</div>
    <div class="photo" style="left:124px;top:35px;width:132px;height:94px;background:linear-gradient(100deg,#c9d2dc,#b5664c 45%,#e6e2dc 70%,#7a879f)" role="img" aria-label="Photo of a discussion group seated in a circle"></div>
    <div class="foot"><span class="firm">Northgate Law P.C.</span><span class="url">Go to www.pollhub.example/danawhitlock</span><span class="num">10</span></div>
  </section>

  <!-- 11 Who is your audience -->
  <section class="slide" aria-label="Who is your audience">
    <div class="photo" style="left:11px;top:0;width:98px;height:131px;background:linear-gradient(90deg,#b3825f,#e3e5ea 55%,#c8ccd6)" role="img" aria-label="Photo of a smiling woman in a striped sweater seated in a group"></div>
    <div class="h2" style="left:122px;top:12px">Who is your Audience ?<br>Who read your guaidance?<br>be specific</div>
    <ol class="numbered" style="left:116px;top:46px;width:140px">
      <li>Lorem Ipsum is simply dummy text of the printing and typesetting industry.</li>
      <li>Lorem Ipsum has been the industry's standard dummy text ever since the 1500s, when an unknown printer took a galley of type and scrambled it to make a type specimen book. It has survived not only five centuries, but also the leap into electronic typesetting, remaining essentially unchanged.</li>
      <li>It was popularized in the 1960s with the release of Lettersheet sheets containing</li>
      <li>Lorem Ipsum passages, and more recently with desktop publishing software like Quill Layout including versions of Lorem Ipsum.</li>
    </ol>
    <div class="foot"><span class="firm">Northgate Law P.C.</span><span class="url">Go to www.pollhub.example/danawhitlock</span><span class="num">11</span></div>
  </section>

  <!-- 12 Readers -->
  <section class="slide" aria-label="Readers of your guidance">
    <div class="h2" style="left:13px;top:17px">Readers of your<br>guidance</div>
    <ul class="bullets tight" style="left:13px;top:42px;width:110px;font-size:4.1px">
      <li>Initial recipient of your email</li>
      <li>Employment or labor lawyer of client</li>
      <li>Other lawyers in the client's legal department</li>
      <li>Human resources professionals</li>
      <li>Executives at your client</li>
      <li>Subject matter experts at Northgate</li>
      <li>All of the above but one year later</li>
    </ul>
    <div class="photo" style="left:125px;top:21px;width:131px;height:98px;background:radial-gradient(ellipse at 60% 60%,#e9d7b0 0%,#9b6b3a 40%,#3d2817 100%)" role="img" aria-label="Photo of an open book on a stack of books in a library"></div>
    <div class="foot"><span class="firm">Northgate Law P.C.</span><span class="url">Go to www.pollhub.example/danawhitlock</span><span class="num">12</span></div>
  </section>

  <!-- 13 Purpose -->
  <section class="slide" aria-label="Purpose">
    <div class="photo" style="left:11px;top:0;width:98px;height:131px;background:linear-gradient(135deg,#c99373,#e7e3df 45%,#cfd6e0)" role="img" aria-label="Photo of a hand filling in a paper test with a pencil"></div>
    <div class="h2" style="left:122px;top:22px">Purpose</div>
    <ul class="bullets" style="left:122px;top:47px;width:130px;font-size:4.4px">
      <li>Information in response to a specific request</li>
      <li>Limitations
        <ul class="sub" style="font-size:3.8px;color:var(--navy);margin-top:3px">
          <li>• Not persuading, not entertaining</li>
          <li>• Request must be appropriately specific</li>
          <li>• Answer must be within your knowledge</li>
          <li>• Answer must meet the deadline</li>
        </ul>
      </li>
    </ul>
    <div class="foot"><span class="firm">Northgate Law P.C.</span><span class="url">Go to www.pollhub.example/danawhitlock</span><span class="num">13</span></div>
  </section>

  <!-- 14 Example 2 long reply -->
  <section class="slide" aria-label="Example 2 long reply">
    <div class="ex-title">Example 2</div>
    <div class="meta">
      <div class="meta-row r1"><span class="k">To</span><span class="v">Sam Holloway<br>RK Holdings</span></div>
      <div class="meta-row r2" style="margin-top:6px"><span class="k" style="height:11px;padding-top:3px">From</span><span class="v">Northgate on Demand</span></div>
      <div class="meta-row r3" style="margin-top:6px"><span class="k">Subject</span><span class="v">Medical Marijuana</span></div>
    </div>
    <div class="mailbox dense" style="top:26px;height:105px">
      <p>Thank you for your question. My apologies for the tardy response. Unfortunately, eliminating employee use of marijuana throughout the entire company may be more easily said than done, implicating as it does a complicated patchwork of federal and state laws that affect employee use of medical marijuana, including but not limited to states with explicit laws granting employees with a documented medical need protections for marijuana use in certain circumstances. Nevada is instructive here: its state law requires employers to make reasonable accommodations for employees holding medical marijuana cards, and the state supreme court recently recognized a private right of action under that statute. Nevertheless, in the time allotted for the response you have requested, we are unable to give you a state-by-state primer on the legality of extinguishing the permissibility of marijuana use among your workforce. You won't be able to prohibit it everywhere, but that much is certain, even though you apparently prohibit it throughout your department. Why? Because some states have established laws that prohibit a company from forbidding employees with a medical need for marijuana to use it. These laws probably exist in some of the states in which you operate and in which you will have employees. Can you send me a list of your states?</p>
      <p>Regards,<br>Nolan</p>
    </div>
    <div class="foot"><span class="firm">Northgate Law P.C.</span><span class="url">Go to www.pollhub.example/danawhitlock</span><span class="num">14</span></div>
  </section>

  <!-- 15 Characteristics billboard -->
  <section class="slide dark" aria-label="Characteristics of a quality response">
    <svg class="wedge" viewBox="0 0 267 150">
      <defs><linearGradient id="envelopes" x1="0" y1="0" x2="1" y2="1"><stop offset="0" stop-color="#b9d3ea"/><stop offset=".45" stop-color="#9cc79a"/><stop offset=".6" stop-color="#e8bcc0"/><stop offset=".78" stop-color="#d9781f"/><stop offset="1" stop-color="#3fa6d6"/></linearGradient></defs>
      <path d="M180,0 H192 L144,60 Q134,75 146,90 L214,150 H202 L134,90 Q122,75 132,60 Z" fill="var(--blue)"/>
      <path d="M192,0 H200 L152,60 Q142,75 154,90 L222,150 H214 L146,90 Q134,75 144,60 Z" fill="#dbe6f4"/>
      <g role="img" aria-label="Photo of colourful paper envelopes on a blue and orange background"><path d="M200,0 H267 V150 H222 L154,90 Q142,75 152,60 Z" fill="url(#envelopes)"/></g>
    </svg>
    <div class="billboard-title" style="top:80px;left:28px">Characteristics<br>of a quality<br>response</div>
    <div class="foot"><span class="firm">Northgate Law P.C.</span><span class="url">Go to www.pollhub.example/danawhitlock</span><span class="num"></span></div>
  </section>

  <!-- 16 Quick -->
  <section class="slide" aria-label="Characteristics of a quality response: Quick">
    <div class="quick-panel">Characteristics of a<br>quality response:<br>Quick</div>
    <div class="q-icon first" style="top:11px;height:38px">
      <svg viewBox="0 0 20 20" width="11" height="11" style="margin-top:9px"><circle cx="10" cy="11" r="7" fill="none" stroke="#fff" stroke-width="1.6"/><rect x="8" y="1.5" width="4" height="2" fill="#fff"/><path d="M10 11 V6.5" stroke="#fff" stroke-width="1.6"/></svg>
      <div>Time</div>
    </div>
    <div class="q-icon" style="top:52px;height:39px">
      <svg viewBox="0 0 20 20" width="11" height="11" style="margin-top:9px"><path d="M1 10 Q10 2 19 10 Q10 18 1 10 Z" fill="none" stroke="#fff" stroke-width="1.6"/><circle cx="10" cy="10" r="3" fill="#fff"/></svg>
      <div>Identify</div>
    </div>
    <div class="q-icon" style="top:94px;height:38px;background:#9eb3d9">
      <svg viewBox="0 0 20 20" width="11" height="11" style="margin-top:8px"><rect x="3" y="1" width="14" height="7" fill="none" stroke="#fff" stroke-width="1.2"/><circle cx="6" cy="12" r="2" fill="#fff"/><circle cx="14" cy="12" r="2" fill="#fff"/><path d="M2 19 Q6 14 10 19 Q14 14 18 19" fill="#fff"/></svg>
      <div>Answer</div>
    </div>
    <div class="q-text" style="top:11px;height:38px;padding-top:12px">On time (after shaping and meeting the expectations)</div>
    <div class="q-text" style="top:52px;height:39px;padding-top:14px">Identify the question (critical for clarity)</div>
    <div class="q-text" style="top:94px;height:38px;padding-top:16px">Answer the question right away</div>
    <div class="foot"><span class="firm">Northgate Law P.C.</span><span class="url">Go to www.pollhub.example/danawhitlock</span><span class="num">16</span></div>
  </section>

  <!-- 17 Example 2 callouts -->
  <section class="slide" aria-label="Example 2 opening callouts">
    <div class="ex-title">Example 2</div>
    <div class="meta">
      <div class="meta-row r1"><span class="k">To</span><span class="v">Sam Holloway<br>RK Holdings</span></div>
      <div class="meta-row r2" style="margin-top:6px"><span class="k" style="height:11px;padding-top:3px">From</span><span class="v">Northgate on Demand</span></div>
      <div class="meta-row r3" style="margin-top:6px"><span class="k">Subject</span><span class="v">Medical Marijuana</span></div>
    </div>
    <div class="mailbox" style="font-size:2.7px">
      <p>Thank you for your question whether RK Holdings may discipline employees who use marijuana (even to treat a medical condition) in the six states where it operates. You may, except in Colorado or Nevada.</p>
    </div>
    <svg class="leader" viewBox="0 0 267 150"><path d="M117 43 L101 93 M144 43 L130 93 M232 43 L206 94" stroke="var(--accent-red)" stroke-width=".4" fill="none"/></svg>
    <div class="callout" style="left:120px;top:93px;width:30px">Restate<br>question</div>
    <div class="callout" style="left:199px;top:94px;width:32px;padding:2px">Quick answer</div>
    <div class="foot"><span class="firm">Northgate Law P.C.</span><span class="url">Go to www.pollhub.example/danawhitlock</span><span class="num">17</span></div>
  </section>

  <!-- 18 Email openers -->
  <section class="slide" aria-label="Email openers">
    <div class="h2" style="left:13px;top:20px">Email openers</div>
    <ul class="bullets tight" style="left:13px;top:44px;width:120px;font-size:3.9px">
      <li>You asked whether ...</li>
      <li>This email responds to your question whether ...</li>
      <li>You requested guidance on the ability of ...</li>
      <li>In your email last week, you explained that ...</li>
      <li>Two of your businesses, I understand, would like to ...</li>
      <li>I have prepared guidance on your proposal to ...</li>
    </ul>
    <div class="photo" style="left:157px;top:0;width:99px;height:131px;background:linear-gradient(160deg,#b8d2ea 0%,#9cc79a 35%,#e8bcc0 55%,#d9781f 75%,#3fa6d6 100%)" role="img" aria-label="Photo of colourful paper envelopes"></div>
    <div class="foot"><span class="firm">Northgate Law P.C.</span><span class="url">Go to www.pollhub.example/danawhitlock</span><span class="num">18</span></div>
  </section>

  <!-- 19 CLEAR -->
  <section class="slide" aria-label="Characteristics of a quality response: Clear">
    <div class="h2 center-h" style="top:11px">Characteristics of a quality response: CLEAR</div>
    <div class="clear-bar" style="top:29px"><svg viewBox="0 0 10 10"><rect x="1" y="1" width="8" height="8" fill="none" stroke="#fff" stroke-width="1"/><path d="M2.8 5 L4.5 6.8 L7.5 3" stroke="#fff" stroke-width="1" fill="none"/></svg>Use short paragraphs</div>
    <div class="clear-bar" style="top:51px"><svg viewBox="0 0 10 10"><circle cx="5" cy="4" r="3.3" fill="#fff"/><rect x="3.6" y="7" width="2.8" height="2.4" fill="#fff"/></svg>Use cues (bullets, numbers, headings, subheadings)</div>
    <div class="clear-bar" style="top:73px"><svg viewBox="0 0 10 10"><path d="M1 9 L2 6 L7.5 0.5 L9.5 2.5 L4 8 Z" fill="#fff"/></svg>Topic sentences – consistently</div>
    <div class="clear-bar" style="top:94px"><svg viewBox="0 0 10 10"><path d="M0.5 1 H9.5 L6 5 V9.5 L4 8.5 V5 Z" fill="#fff"/></svg>Include information in descending order of importance</div>
    <div class="clear-bar" style="top:116px"><svg viewBox="0 0 10 10"><rect x="1" y="1" width="3.5" height="3.5" fill="#fff"/><rect x="5.5" y="5.5" width="3.5" height="3.5" fill="#fff"/><rect x="1" y="5.5" width="3.5" height="3.5" fill="none" stroke="#fff" stroke-width=".8"/><rect x="5.5" y="1" width="3.5" height="3.5" fill="none" stroke="#fff" stroke-width=".8"/></svg>Identify any assumptions and key facts</div>
    <div class="foot"><span class="firm">Northgate Law P.C.</span><span class="url">Go to www.pollhub.example/danawhitlock</span><span class="num">19</span></div>
  </section>

  <!-- 20 Example 2 structure callouts -->
  <section class="slide" aria-label="Example 2 structure callouts">
    <div class="ex-title">Example 2</div>
    <div class="meta">
      <div class="meta-row r1"><span class="k">To</span><span class="v">Sam Holloway<br>RK Holdings</span></div>
      <div class="meta-row r2" style="margin-top:6px"><span class="k" style="height:11px;padding-top:3px">From</span><span class="v">Northgate on Demand</span></div>
      <div class="meta-row r3" style="margin-top:6px"><span class="k">Subject</span><span class="v">Medical Marijuana</span></div>
    </div>
    <div class="mailbox dense" style="font-size:2.5px;padding:5px 6px">
      <p>Thank you for your question whether RK Holdings may discipline employees who use marijuana – even to treat a medical condition – in the six states where it operates. You may, except in Colorado or Nevada.</p>
      <p>RK Holdings, I understand, employs personnel in Alabama, Colorado, Florida, Mississippi, Louisiana, and Nevada. This advice does not address whether the Company's past or current practices concerning marijuana use comply with federal or state law.</p>
      <p>Prohibition Allowed in Alabama, Florida, Mississippi, and Louisiana. In these four states, you may prohibit employees from appearing at work under the influence of marijuana or using marijuana at work. To enforce that rule, you may randomly test your employees and discipline those who fail a test, provided that the Company implements an appropriately designed testing program. We can help you develop a drug testing program; just let us know.</p>
      <p>The laws in three of these states – Alabama, Mississippi, and Louisiana – do not permit the recreational or medical use of marijuana. Florida citizens may use marijuana to treat a medical condition, but they are not entitled to work under the influence of marijuana.</p>
    </div>
    <svg class="leader" viewBox="0 0 267 150"><path d="M94 74 L98 123 M125 92 L128 130 M166 92 L170 121 M172 100 L206 126 M246 60 L244 121" stroke="var(--accent-red)" stroke-width=".4" fill="none"/></svg>
    <div class="callout" style="left:92px;top:121px;width:17px">Assumed<br>facts</div>
    <div class="callout" style="left:128px;top:129px;width:19px">Out of scope</div>
    <div class="callout" style="left:161px;top:121px;width:16px;padding:1.5px">Cues</div>
    <div class="callout" style="left:196px;top:126px;width:17px">Topic<br>sentence</div>
    <div class="callout" style="left:233px;top:121px;width:20px">Short<br>paragraphs</div>
    <div class="foot"><span class="firm">Northgate Law P.C.</span><span class="url">Go to www.pollhub.example/danawhitlock</span><span class="num">20</span></div>
  </section>

</main>
</body>
</html>
```